Dental Business Card

I need Dental oriented business cards.
On the front side -
- on the first line, my name:
Dr Marlo Vintner
- on the second line (just underneath):
Doctor of Dental Medicine
- on the third line, or underneath that or in a corner, I would like the address and phone number:
5182 Ch. Birchfield
Montreal QC H2T 4B9
514-629-5074
- other than that i would maybe like a logo of a tooth, but i want it to be subtle and very basic!
- I would like the card to be preferably black or dark grey-ish with the writing in white
On the other side -
- 2-3 lines with the possibility to write the next appointment the box with the lines should be white, with the rest of the card being black

```html
<!DOCTYPE html>
<html lang="en">
<head>
<meta charset="utf-8">
<title>Dental Business Card – Dr Marlo Vintner</title>
<link rel="stylesheet" href="https://fonts.googleapis.com/css2?family=Montserrat:wght@300&family=Quicksand:wght@700&display=swap">
<style>
  :root {
    --backdrop: #151515;
    --card: #202020;
    --ink: #f2f2f2;
    --ink-soft: #d6d6d6;
    --note: #efefef;
  }
  * { margin: 0; padding: 0; box-sizing: border-box; }
  html, body {
    width: 1200px;
    height: 1200px;
    overflow: hidden;
    background: var(--backdrop);
  }
  .canvas {
    position: relative;
    width: 1200px;
    height: 1200px;
  }
  .card {
    position: absolute;
    left: 228px;
    width: 748px;
    height: 424px;
    background: var(--card);
    border-radius: 40px;
    box-shadow: 0 10px 24px rgba(0,0,0,0.55);
  }
  .card--front { top: 136px; }
  .card--back  { top: 640px; }

  .contact {
    position: absolute;
    left: 86px;
    top: 104px;
    color: var(--ink-soft);
    font-family: "Montserrat", sans-serif;
    font-weight: 300;
    font-size: 19px;
    letter-spacing: 0.4px;
    line-height: 1.4;
  }
  .contact__name {
    font-family: "Quicksand", sans-serif;
    font-weight: 700;
    font-size: 27px;
    color: var(--ink);
    letter-spacing: 0.2px;
    line-height: 1.2;
    margin-bottom: 2px;
  }
  .contact__phone { margin-top: 34px; }
  .contact__address { margin-top: 32px; line-height: 1.4; }

  .practice-mark {
    position: absolute;
    border: 2px solid var(--ink);
    border-radius: 50%;
    display: flex;
    align-items: center;
    justify-content: center;
    text-align: center;
    color: var(--ink);
    font-family: "Montserrat", sans-serif;
    font-weight: 300;
    letter-spacing: 1px;
    line-height: 1.3;
  }
  .card--front .practice-mark {
    left: 460px;
    top: 112px;
    width: 200px;
    height: 200px;
    font-size: 18px;
  }
  .card--back .practice-mark {
    left: 300px;
    top: 46px;
    width: 148px;
    height: 148px;
    font-size: 14px;
  }

  .appointment-box {
    position: absolute;
    left: 34px;
    top: 244px;
    width: 676px;
    height: 146px;
    background: var(--note);
    border-radius: 30px;
  }
</style>
</head>
<body>
<main class="canvas">
  <section class="card card--front">
    <div class="contact">
      <p class="contact__name">Dr Marlo Vintner</p>
      <p class="contact__title">Doctor of Dental Medicine</p>
      <p class="contact__phone">514-629-5074</p>
      <p class="contact__address">5182 Ch. Birchfield<br>Montreal QC H2T 4B9</p>
    </div>
    <div class="practice-mark">Vintner<br>Dental</div>
  </section>

  <section class="card card--back">
    <div class="practice-mark">Vintner<br>Dental</div>
    <div class="appointment-box"></div>
  </section>
</main>
</body>
</html>
```